Updated Stationary needed using new logo for Hair Tissue Mineral Analysis Company

Simple stationary design needed using new logo!
1. 8.5" x 11" Letterhead with company information listed below
2. 8.5" x 11" Design with Footer only with logo and information for print materials
3. 5.5" x 8.5" letterhead design
4. 4.125" x 9.5" Business envelope (#10 envelope) with address
5. 4.125" x 9.5" Business envelope with clear window (#10 envelope) with address
6. 6.5" x 9.5" envelope (6 3/4 Booklet envelope) with address
7. 10" x 13" Open End envelope
Address:
4817 N. Corwin Street
Larkdale, AZ 85390
Phone:
(602)-417-3926
Website:
www.pexumor.com
Email:
information@pexumor.com
Updates
Need extra days to review
Focused on completing other projects first
Look and feel
Each slider illustrates characteristics of the customer's brand and the style your logo design should communicate.

```html
<!DOCTYPE html>
<html lang="en">
<head>
<meta charset="utf-8">
<title>Pexumor Labs Stationery</title>
<link rel="stylesheet" href="https://fonts.googleapis.com/css2?family=Titillium+Web:wght@400;700&display=swap">
<style>
  :root {
    --backdrop: #48bdc3;
    --paper: #ffffff;
    --navy: #13224f;
    --blue: #2f58a3;
    --sky: #5b82c9;
    --orange: #f58220;
    --ink: #1a2550;
  }
  * { margin: 0; padding: 0; box-sizing: border-box; }
  html, body { width: 1200px; height: 719px; overflow: hidden; }
  body {
    position: relative;
    background: var(--backdrop);
    font-family: "Titillium Web", sans-serif;
  }
  .sheet {
    position: absolute;
    background: var(--paper);
    overflow: hidden;
  }
  .sheet svg.bands { position: absolute; left: 0; top: 0; }
  .brand {
    position: absolute;
    display: flex;
    align-items: center;
    gap: 0.35em;
    font-family: "Titillium Web", sans-serif;
    font-weight: 700;
    color: var(--blue);
    letter-spacing: 0.02em;
    white-space: nowrap;
    line-height: 1;
  }
  .brand .dot {
    width: 0.7em; height: 0.7em;
    border-radius: 50%;
    background: currentColor;
  }
  .brand.on-dark { color: #ffffff; }
  .contact {
    position: absolute;
    list-style: none;
    text-align: right;
    color: var(--ink);
    line-height: var(--lh);
    font-size: var(--fs);
  }
  .contact.on-dark { color: #ffffff; }
  .contact li {
    display: flex;
    justify-content: flex-end;
    align-items: center;
    gap: calc(var(--fs) * 1.1);
    white-space: nowrap;
  }
  .contact .icon {
    width: calc(var(--fs) * 0.95);
    height: calc(var(--fs) * 0.95);
    border: 1px solid var(--orange);
    border-radius: 50%;
    flex: none;
    position: relative;
  }
  .contact .icon::after {
    content: "";
    position: absolute;
    left: 28%; top: 28%;
    width: 44%; height: 44%;
    background: var(--orange);
    border-radius: 50%;
  }
  .contact .no-icon { width: calc(var(--fs) * 0.95); flex: none; }
  .address-window {
    position: absolute;
    background: #30599f;
    border-radius: 8px;
  }
</style>
</head>
<body>

<!-- Letterhead with footer -->
<section class="sheet letter-footer" style="left:33px; top:29px; width:324px; height:420px;">
  <svg class="bands" width="324" height="420" viewBox="0 0 324 420">
    <polygon points="0,353 66,353 77,364 0,364" fill="var(--navy)"/>
    <polygon points="66,353 136,353 147,364 77,364" fill="var(--orange)"/>
    <rect x="147" y="358" width="177" height="6" fill="var(--sky)"/>
    <rect x="0" y="364" width="324" height="56" fill="var(--navy)"/>
  </svg>
  <div class="brand on-dark" style="left:11px; top:380px; font-size:20px;"><span class="dot"></span>Pexumor Labs</div>
  <ul class="contact on-dark" style="right:24px; top:369px; --fs:6.6px; --lh:9.6px;">
    <li>(602)-417-3926<span class="icon"></span></li>
    <li>information@pexumor.com<span class="icon"></span></li>
    <li>www.pexumor.com<span class="icon"></span></li>
    <li>4817 N. Corwin Street<span class="icon"></span></li>
    <li>Larkdale, AZ 85390<span class="no-icon"></span></li>
  </ul>
</section>

<!-- #10 business envelope -->
<section class="sheet envelope-10" style="left:429px; top:29px; width:363px; height:158px;">
  <svg class="bands" width="363" height="158" viewBox="0 0 363 158">
    <rect x="0" y="147" width="280" height="6" fill="var(--sky)"/>
    <polygon points="290,141 327,141 313,153 275,153" fill="var(--orange)"/>
    <polygon points="327,141 363,141 363,153 313,153" fill="var(--navy)"/>
    <rect x="0" y="153" width="363" height="5" fill="var(--navy)"/>
  </svg>
  <div class="brand" style="left:11px; top:12px; font-size:18px;"><span class="dot"></span>Pexumor Labs</div>
  <ul class="contact" style="right:11px; top:82px; --fs:7.6px; --lh:11px;">
    <li>(602)-417-3926<span class="icon"></span></li>
    <li>information@pexumor.com<span class="icon"></span></li>
    <li>www.pexumor.com<span class="icon"></span></li>
    <li>4817 N. Corwin Street<span class="icon"></span></li>
    <li>Larkdale, AZ 85390<span class="no-icon"></span></li>
  </ul>
</section>

<!-- #10 window envelope -->
<section class="sheet envelope-10-window" style="left:429px; top:202px; width:363px; height:158px;">
  <svg class="bands" width="363" height="158" viewBox="0 0 363 158">
    <rect x="0" y="147" width="280" height="6" fill="var(--sky)"/>
    <polygon points="290,141 327,141 313,153 275,153" fill="var(--orange)"/>
    <polygon points="327,141 363,141 363,153 313,153" fill="var(--navy)"/>
    <rect x="0" y="153" width="363" height="5" fill="var(--navy)"/>
  </svg>
  <div class="brand" style="left:11px; top:12px; font-size:18px;"><span class="dot"></span>Pexumor Labs</div>
  <div class="address-window" style="left:25px; top:55px; width:164px; height:73px;"></div>
  <ul class="contact" style="right:11px; top:82px; --fs:7.6px; --lh:11px;">
    <li>(602)-417-3926<span class="icon"></span></li>
    <li>information@pexumor.com<span class="icon"></span></li>
    <li>www.pexumor.com<span class="icon"></span></li>
    <li>4817 N. Corwin Street<span class="icon"></span></li>
    <li>Larkdale, AZ 85390<span class="no-icon"></span></li>
  </ul>
</section>

<!-- 5.5 x 8.5 letterhead -->
<section class="sheet letter-half" style="left:427px; top:376px; width:210px; height:325px;">
  <svg class="bands" width="210" height="325" viewBox="0 0 210 325">
    <rect x="0" y="0" width="210" height="38" fill="var(--navy)"/>
    <polygon points="0,38 46,38 42,44 0,44" fill="var(--navy)"/>
    <polygon points="46,38 95,38 91,44 42,44" fill="var(--orange)"/>
    <rect x="95" y="38" width="115" height="4" fill="var(--sky)"/>
    <rect x="0" y="317" width="165" height="4" fill="var(--sky)"/>
    <polygon points="168,315 191,315 184,321 161,321" fill="var(--orange)"/>
    <polygon points="191,315 210,315 210,321 184,321" fill="var(--navy)"/>
    <rect x="0" y="321" width="210" height="4" fill="var(--navy)"/>
  </svg>
  <div class="brand on-dark" style="left:9px; top:12px; font-size:13px;"><span class="dot"></span>Pexumor Labs</div>
  <ul class="contact on-dark" style="right:14px; top:5px; --fs:3.9px; --lh:6.2px;">
    <li>(602)-417-3926<span class="icon"></span></li>
    <li>information@pexumor.com<span class="icon"></span></li>
    <li>www.pexumor.com<span class="icon"></span></li>
    <li>4817 N. Corwin Street<span class="icon"></span></li>
    <li>Larkdale, AZ 85390<span class="no-icon"></span></li>
  </ul>
</section>

<!-- 8.5 x 11 letterhead -->
<section class="sheet letter-full" style="left:855px; top:20px; width:325px; height:420px;">
  <svg class="bands" width="325" height="420" viewBox="0 0 325 420">
    <rect x="0" y="0" width="325" height="56" fill="var(--navy)"/>
    <polygon points="0,56 73,56 65,67 0,67" fill="var(--navy)"/>
    <polygon points="73,56 148,56 138,67 65,67" fill="var(--orange)"/>
    <rect x="148" y="56" width="177" height="5" fill="var(--sky)"/>
    <rect x="0" y="409" width="258" height="5" fill="var(--sky)"/>
    <polygon points="262,404 291,404 280,414 251,414" fill="var(--orange)"/>
    <polygon points="291,404 325,404 325,414 280,414" fill="var(--navy)"/>
    <rect x="0" y="414" width="325" height="6" fill="var(--navy)"/>
  </svg>
  <div class="brand on-dark" style="left:17px; top:17px; font-size:20px;"><span class="dot"></span>Pexumor Labs</div>
  <ul class="contact on-dark" style="right:26px; top:8px; --fs:6.5px; --lh:9.6px;">
    <li>(602)-417-3926<span class="icon"></span></li>
    <li>information@pexumor.com<span class="icon"></span></li>
    <li>www.pexumor.com<span class="icon"></span></li>
    <li>4817 N. Corwin Street<span class="icon"></span></li>
    <li>Larkdale, AZ 85390<span class="no-icon"></span></li>
  </ul>
</section>

<!-- 6 3/4 booklet envelope -->
<section class="sheet envelope-booklet" style="left:817px; top:460px; width:363px; height:248px;">
  <svg class="bands" width="363" height="248" viewBox="0 0 363 248">
    <rect x="0" y="236" width="280" height="6" fill="var(--sky)"/>
    <polygon points="290,231 327,231 313,242 275,242" fill="var(--orange)"/>
    <polygon points="327,231 363,231 363,242 313,242" fill="var(--navy)"/>
    <rect x="0" y="242" width="363" height="6" fill="var(--navy)"/>
  </svg>
  <div class="brand" style="left:16px; top:15px; font-size:18px;"><span class="dot"></span>Pexumor Labs</div>
  <ul class="contact" style="right:11px; top:173px; --fs:7.6px; --lh:11px;">
    <li>(602)-417-3926<span class="icon"></span></li>
    <li>information@pexumor.com<span class="icon"></span></li>
    <li>www.pexumor.com<span class="icon"></span></li>
    <li>4817 N. Corwin Street<span class="icon"></span></li>
    <li>Larkdale, AZ 85390<span class="no-icon"></span></li>
  </ul>
</section>

</body>
</html>
```